Etiketten-Design für Gin- und Rumhersteller
Zielgruppe
Zielgruppe 20-35 Jahre, Wir sind ein Gin- und Rumhersteller und hätten gerne ein Etikett für unsere Flaschen. Etikett-Maße jeweils 70 x 70 mm.
Aufgabenstellung
Schwarzweißes Design, eventuell mit Gold oder Silber, Etikett selbst schwarz. Junger moderner Stil, Das Logo soll Groß auf dem Etikett sichtbar sein. Es gibt nur eine Vorderseite. Maße 70 x 70 mm.
Etikett Aufbau :
Wolkenhof (Groß, Logo anbei)
GIN oder RUM
40% Alk
hergestellt & abgefüllt in Vorarlberg
Wolkenhof Gin
aus der Firmengruppe der
HausKontor (Klein, Logo anbei)

```html
<!DOCTYPE html>
<html lang="de">
<head>
<meta charset="utf-8">
<title>Wolkenhof Etiketten</title>
<link href="https://fonts.googleapis.com/css2?family=Federo&family=Oswald:wght@500&display=swap" rel="stylesheet">
<style>
  :root {
    --canvas: #5d6166;
    --label-bg: #272727;
    --gold: #c9a45c;
    --gold-light: #f3e4a6;
    --silver: #c9c9c9;
    --silver-light: #f2f2f2;
    --seal-green: #2d8b3e;
    --brand-green: #1d8a33;
  }
  * { margin: 0; padding: 0; box-sizing: border-box; }
  html, body { width: 1200px; height: 1080px; overflow: hidden; }
  body { background: var(--canvas); position: relative; font-family: "Federo", sans-serif; }

  .label {
    position: absolute;
    top: 191px;
    width: 499px;
    height: 499px;
    background: var(--label-bg);
    border: 4px solid var(--metal);
  }
  .label--gin { left: 87px; --metal: var(--gold); --metal-light: var(--gold-light); }
  .label--rum { left: 630px; --metal: var(--silver); --metal-light: var(--silver-light); }

  .label__origin {
    position: absolute;
    left: 29px; top: 22px;
    font-size: 19px;
    color: var(--metal);
    letter-spacing: 0.3px;
    white-space: nowrap;
  }
  .label__brand {
    position: absolute;
    left: 0; right: 40px; top: 70px;
    text-align: center;
    font-size: 82px;
    font-weight: 400;
    line-height: 1;
    color: var(--metal);
    white-space: nowrap;
  }
  .label__ornament {
    position: absolute;
    left: 44px; top: 290px;
    width: 420px; height: 76px;
    border-radius: 38px;
    background: linear-gradient(90deg, var(--metal), var(--metal-light) 50%, var(--metal) 80%, var(--label-bg));
  }
  .label__seal {
    position: absolute;
    left: 174px; top: 200px;
    width: 150px; height: 150px;
    border-radius: 50%;
    background: var(--seal-green);
  }
  .label__kind {
    position: absolute;
    left: 174px; top: 236px; width: 150px;
    text-align: center;
    font-family: "Oswald", sans-serif;
    font-weight: 500;
    font-size: 70px;
    line-height: 1;
    color: var(--metal);
  }
  .label--rum .label__kind { color: #e9e9e9; }
  .label__group {
    position: absolute;
    left: 29px; top: 434px;
    font-size: 20px;
    color: var(--metal);
    letter-spacing: 1px;
    white-space: nowrap;
  }
  .label__partner {
    position: absolute;
    right: 0; bottom: 0;
    width: 42px; height: 190px;
    background: var(--metal);
  }
  .label__partner-name {
    position: absolute;
    left: 50%; top: 95px;
    transform: translate(-50%, -50%) rotate(-90deg);
    width: 170px; height: 26px;
    text-align: center;
    font-size: 21px;
    line-height: 26px;
    color: var(--brand-green);
    white-space: nowrap;
  }
</style>
</head>
<body>

<section class="label label--gin">
  <p class="label__origin">40% Alk hergestellt &amp; abgefüllt in Vorarlberg</p>
  <h1 class="label__brand">Wolkenhof</h1>
  <div class="label__ornament" role="img" aria-label="Goldener Pinselstrich als Schmuckelement"></div>
  <div class="label__seal"></div>
  <div class="label__kind">GIN</div>
  <p class="label__group">Wolkenhof Gin aus der Firmengruppe der</p>
  <div class="label__partner"><span class="label__partner-name">HausKontor</span></div>
</section>

<section class="label label--rum">
  <p class="label__origin">40% Alk hergestellt &amp; abgefüllt in Vorarlberg</p>
  <h1 class="label__brand">Wolkenhof</h1>
  <div class="label__ornament" role="img" aria-label="Silberner Pinselstrich als Schmuckelement"></div>
  <div class="label__seal"></div>
  <div class="label__kind">RUM</div>
  <p class="label__group">Wolkenhof Gin aus der Firmengruppe der</p>
  <div class="label__partner"><span class="label__partner-name">HausKontor</span></div>
</section>

</body>
</html>
```